Please look at my website to get a better understanding of my business: www.perovatu.com
This business is about Life Coaching for Families, couples, teenagers and individuals. I work more w parents of teenagers (as well as teenagers) but not so much with young kids.
The card should be fun, not too busy, with a sense of flow and playfulness. Warm colors, artistic style (can have a family sculpture, paining or a picture in it). Basic information about myself and my company

Reason: I extended my due date for next Tuesday, November 13th. Please summit new designs if you haven't done so, and for those who submitted, thank you so much for your time and effort. I will make a decision next Tues, and will contact you if I need to revise some items. Much thanks to you all! Orla

Families, parents, teenagers, couples, individuals.

Business

• Business name: PeRoVaTu! Hearth Circle Life Coaching
My name: Orla Bekwith, RMTQ
Description of my work: Tri-Mode life coach
Tel: 555-304-7719
Website: www.PeRoVaTu.com
• Family sculpture, abstract painting or a picture, or simply a nice background w/out a picture added.
• Corporate feeling, cold colors, corporate symbols. no Sunset, or picture of families on the beach.
Don't include bar-code (from uploaded file 1, it is only the designer to find out more about my website).

```html
<!DOCTYPE html>
<html lang="en">
<head>
<meta charset="utf-8">
<title>PeRoVaTu Business Card</title>
<link rel="stylesheet" href="https://fonts.googleapis.com/css2?family=Encode+Sans+Semi+Condensed:wght@400;500&display=swap">
<style>
  :root {
    --backdrop: #ecedec;
    --card-gold: #d19b3f;
    --band-rust: #b85a26;
    --band-red: #b83226;
    --ink-red: #b8362a;
    --ink-phone: #cc4a2c;
    --ink-white: #ffffff;
  }
  html, body {
    margin: 0;
    padding: 0;
    width: 1200px;
    height: 900px;
    overflow: hidden;
    background: var(--backdrop);
  }
  .canvas {
    position: relative;
    width: 1200px;
    height: 900px;
  }
  .business-card {
    position: absolute;
    left: 100px;
    top: 170px;
    width: 1000px;
    height: 559px;
    display: block;
  }
  .card-text {
    font-family: "Encode Sans Semi Condensed", "Arial Narrow", sans-serif;
    font-weight: 400;
  }
  .card-base { fill: var(--card-gold); }
  .band-rust { fill: var(--band-rust); }
  .band-red { fill: var(--band-red); }
  .company-name, .company-tagline { fill: var(--ink-red); font-size: 17px; }
  .person-name { fill: var(--ink-white); font-size: 22px; }
  .person-credential { font-size: 17px; }
  .person-role { fill: var(--ink-white); font-size: 18px; }
  .name-rule { stroke: var(--ink-white); stroke-width: 1.4; }
  .contact-phone { fill: var(--ink-phone); font-size: 17px; }
  .contact-web { fill: var(--ink-white); font-size: 17px; }
</style>
</head>
<body>
<main class="canvas">
  <svg class="business-card" viewBox="0 0 531 297" xmlns="http://www.w3.org/2000/svg" role="group" aria-label="Business card for PeRoVaTu, Hearth Circle Life Coaching">
    <rect class="card-base" x="0" y="0" width="531" height="297"/>
    <polygon class="band-rust" points="413,0 531,0 531,297 294,297"/>
    <polygon class="band-red" points="531,25 531,297 421,297"/>

    <g class="card-text">
      <text class="company-name" x="67" y="70">PeRoVaTu</text>
      <text class="company-tagline" x="67" y="92">Hearth Circle Life Coaching</text>

      <line class="name-rule" x1="0" y1="201" x2="67" y2="201"/>
      <text class="person-name" x="67" y="219">Orla Bekwith, <tspan class="person-credential">RMTQ</tspan></text>
      <text class="person-role" x="67" y="244">Tri-Mode life coach</text>

      <text class="contact-phone" x="0" y="0" transform="translate(411 277) rotate(-67)" textLength="180" lengthAdjust="spacingAndGlyphs">Tel: 555-304-7719</text>
      <text class="contact-web" x="0" y="0" transform="translate(448 273) rotate(-67)" textLength="174" lengthAdjust="spacingAndGlyphs">www.perovatu.com</text>
    </g>
  </svg>
</main>
</body>
</html>
```